KTV - FlowFest 2022 Tradfe show 10'Wx8' display

My company Calibrated Works & Supplies, inc. ( K.T.V) has a display booth at the 2022 Virginia flow fest water wastewater trade show next month and would like new backdrop art for our 10'x8' banner stand. our website is
www.ktv-oakdale.example and our company line card is attached to give an idea of what we do. We want the main takeaway from the artwork to let customers know we offer Pumps, Blowers, Motors , Drives & Repair Services for the Municipal water & wastewater industry. Needs this in a high res pdf.

```html
<!DOCTYPE html>
<html lang="en">
<head>
<meta charset="utf-8">
<title>KTV – FlowFest 2022 Backdrop</title>
<link rel="stylesheet" href="https://fonts.googleapis.com/css2?family=Montserrat:wght@300;400;600;700;800&display=swap">
<style>
  :root {
    --page: #e8e8e8;
    --navy: #0d4c93;
    --navy-deep: #0a3670;
    --blue-bright: #1a7fd8;
    --orange: #f77c12;
    --white: #ffffff;
    --ink: #1b1b1b;
  }
  * { margin: 0; padding: 0; box-sizing: border-box; }
  html, body { width: 800px; height: 1200px; overflow: hidden; background: var(--page); }
  body { font-family: "Montserrat", sans-serif; position: relative; }

  .backdrop {
    position: absolute; left: 20px; top: 296px;
    width: 760px; height: 608px; overflow: hidden;
    background: linear-gradient(100deg, var(--navy) 0%, var(--navy) 45%, var(--navy-deep) 100%);
    box-shadow: 0 10px 24px rgba(0,0,0,0.25);
  }
  .backdrop-shapes { position: absolute; inset: 0; }

  .plant-photo {
    position: absolute; left: 380px; top: 0; width: 380px; height: 608px;
    background: linear-gradient(90deg, rgba(13,76,147,0) 0%, rgba(20,60,110,0.55) 40%, rgba(12,40,85,0.7) 100%);
  }

  .headline { position: absolute; left: 29px; top: 48px; color: var(--white); }
  .headline .year { font-weight: 300; font-size: 66px; line-height: 1; letter-spacing: 1px; }
  .headline .event { font-weight: 300; font-size: 40px; line-height: 1.05; margin-top: 4px; letter-spacing: -0.8px; }
  .headline .theme { font-weight: 800; font-size: 47px; line-height: 1.08; letter-spacing: -1.6px; }

  .tagline {
    position: absolute; left: 29px; top: 309px;
    color: var(--white); font-weight: 700; font-size: 18.5px; line-height: 1.3; letter-spacing: 0.3px;
  }

  .services { position: absolute; left: 0; top: 420px; width: 400px; height: 90px; list-style: none; }
  .service { position: absolute; width: 90px; text-align: center; color: var(--white); font-weight: 700; font-size: 17px; }
  .service .icon {
    display: block; width: 56px; height: 56px; margin: 0 auto 10px;
    border-radius: 50%; background: var(--white); border: 2px solid var(--orange);
    box-shadow: 0 0 0 2px var(--white);
  }
  .service.pumps { left: 24px; }
  .service.blowers { left: 116px; }
  .service.motors { left: 208px; }
  .service.drives { left: 294px; }

  .website {
    position: absolute; left: 34px; top: 543px;
    color: var(--ink); font-weight: 700; font-size: 18px; letter-spacing: 1.2px;
  }

  .brand {
    position: absolute; left: 520px; top: 66px;
    color: var(--white); font-weight: 800; font-size: 64px; line-height: 1; letter-spacing: 2px;
  }

  .technician-photo {
    position: absolute; left: 462px; top: 140px; width: 240px; height: 468px;
    border-radius: 110px 110px 0 0;
    background: linear-gradient(180deg, #6f6a4f 0%, #7b7d5c 45%, #b69b3a 78%, #7b7d5c 100%);
  }
</style>
</head>
<body>
  <main class="backdrop">
    <div class="plant-photo" role="img" aria-label="Photo of a water treatment plant interior with pipes and pumps, tinted blue"></div>

    <svg class="backdrop-shapes" viewBox="0 0 760 608" width="760" height="608" aria-hidden="true">
      <line x1="29" y1="288" x2="418" y2="288" stroke="#ffffff" stroke-opacity="0.45" stroke-width="1"/>
      <rect x="61" y="285" width="73" height="7" rx="3.5" fill="#ffffff"/>
      <path d="M0 395 Q140 360 250 387 Q130 380 0 414 Z" fill="#ffffff"/>
      <path d="M0 418 Q240 370 500 470 L500 525 L0 525 Z" fill="#f77c12"/>
      <path d="M420 452 Q640 470 740 608 L660 608 Q600 520 420 452 Z" fill="#1a7fd8"/>
      <rect x="0" y="525" width="500" height="83" fill="#ffffff"/>
    </svg>

    <div class="technician-photo" role="img" aria-label="Photo of a smiling technician in olive coveralls with a yellow tool belt, gesturing toward the services"></div>

    <header class="headline">
      <div class="year">2022</div>
      <div class="event">VIRGINIA FLOW</div>
      <div class="theme">FEST WATER<br>WASTEWATER</div>
    </header>

    <p class="tagline">Repair Services for the Municipal<br>water &amp; wastewater industry</p>

    <ul class="services">
      <li class="service pumps"><span class="icon" role="img" aria-label="Pump icon"></span>Pumps</li>
      <li class="service blowers"><span class="icon" role="img" aria-label="Blower icon"></span>Blowers</li>
      <li class="service motors"><span class="icon" role="img" aria-label="Motor icon"></span>Motors</li>
      <li class="service drives"><span class="icon" role="img" aria-label="Drive icon"></span>Drives</li>
    </ul>

    <p class="website">www.ktv-oakdale.example</p>

    <div class="brand">KTV</div>
  </main>
</body>
</html>
```